Machine shop looking for a Brochure about us

We are Tarvel Tooling a growing machine shop in CT that is in need of a Brochure about us.

the Brochure will be a single flip book (4 pages in total)

The first page will be just our logo and our slogan with few machined parts. Something like the picture that is attached to this.

The second page will be about the company and our quality policy.

The third page will be about the machines we have and our capacity.

And the back side I would like to keep simple maybe the logo in the back again with few good words. any suggestions would be preferred .
Updates

Hello all designers and the Flyers are looking really good! few quick things. we are a machine shop that make parts for all different kinds of industries and just not airplane companies so a generic milling machine or generic machined parts work better for pictures on the flyers. Also, I am not sure how some designers are using Tarvel Fabrication instead of Tarvel tooling for information. Anyhow they are looking really good and we will be picking the designer this Tuesday.

Target Market(s)

venders and customers

Industry/Entity Type

Shop

Font styles to use
Sans Serif

Colors
0255a3
fbed22

Requirements
Must have
• must use our logo colors
• state that we are as9100 certified and also iso 9001
• please email me for more information and questions. I attached a business plan that you can work from.

```html
<!DOCTYPE html>
<html lang="en">
<head>
<meta charset="utf-8">
<title>Tarvel Tooling – Mega-Equipped Shop</title>
<link href="https://fonts.googleapis.com/css2?family=Saira:wght@300;400&family=Saira+Semi+Condensed:wght@500;600&display=swap" rel="stylesheet">
<style>
  :root {
    --navy: #2b2a86;
    --ink: #2a2a2a;
    --grey: #4a4a4a;
    --yellow: #fdd000;
    --badge-red: #c8161d;
    --white: #ffffff;
  }
  * { margin: 0; padding: 0; box-sizing: border-box; }
  html, body { width: 849px; height: 1200px; overflow: hidden; background: var(--white); }
  .page {
    position: relative;
    width: 849px;
    height: 1200px;
    overflow: hidden;
    background: var(--white);
    font-family: "Saira", sans-serif;
  }
  .hero {
    position: absolute;
    left: 0; top: 0;
    width: 849px; height: 556px;
    background:
      radial-gradient(ellipse at 70% 55%, #d9dcdf 0%, #9ea3a8 35%, #4b4f54 70%, #1c1e21 100%);
  }
  .cert {
    position: absolute;
    left: 696px; top: 58px;
    color: var(--white);
    font-family: "Saira Semi Condensed", sans-serif;
    font-weight: 500;
    font-size: 16px;
    line-height: 22px;
  }
  .cert-badge {
    width: 83px; height: 122px;
    background: var(--badge-red);
    margin-bottom: 8px;
  }
  .deco-circle {
    position: absolute;
    left: 650px; top: 950px;
    width: 420px; height: 420px;
    border-radius: 50%;
    background: var(--yellow);
  }
  .intro {
    position: absolute;
    left: 131px; top: 606px;
  }
  .intro-title {
    font-family: "Saira Semi Condensed", sans-serif;
    font-weight: 600;
    font-size: 37px;
    line-height: 50px;
    color: var(--navy);
    letter-spacing: 0.2px;
  }
  .intro-subtitle {
    font-weight: 300;
    font-size: 17.5px;
    color: var(--grey);
    letter-spacing: 0.3px;
    margin-top: 2px;
  }
  .capability {
    position: absolute;
    left: 128px;
    width: 520px;
    display: flex;
  }
  .capability-icon { width: 124px; flex: none; padding-top: 6px; }
  .capability-title {
    font-family: "Saira Semi Condensed", sans-serif;
    font-weight: 600;
    font-size: 15.5px;
    color: var(--navy);
    line-height: 22px;
    margin-bottom: 1px;
  }
  .capability-text {
    font-weight: 400;
    font-size: 14.6px;
    line-height: 23.6px;
    color: var(--ink);
    width: 370px;
  }
  .capability--lathes { top: 712px; }
  .capability--milling { top: 846px; }
  .capability--finishing { top: 979px; }
</style>
</head>
<body>
<main class="page">
  <div class="hero" role="img" aria-label="Close-up photograph of a CNC milling cutter machining a metal part"></div>

  <div class="cert">
    <div class="cert-badge" aria-hidden="true"></div>
    <div>AS9100</div>
    <div>Aerospace</div>
  </div>

  <div class="deco-circle" aria-hidden="true"></div>

  <header class="intro">
    <h1 class="intro-title">MEGA-EQUIPPED SHOP</h1>
    <p class="intro-subtitle">BUILT FOR QUALITY COMPONENT TOOLING + TIGHT TURNAROUND</p>
  </header>

  <section class="capability capability--lathes">
    <div class="capability-icon">
      <svg width="92" height="62" viewBox="0 0 92 62" fill="var(--navy)" aria-hidden="true">
        <rect x="0" y="2" width="12" height="22"/>
        <rect x="4" y="24" width="84" height="6"/>
        <rect x="48" y="10" width="18" height="12"/>
        <rect x="78" y="6" width="10" height="18"/>
        <rect x="12" y="10" width="36" height="4"/>
        <rect x="6" y="30" width="14" height="30"/>
        <rect x="72" y="30" width="14" height="30"/>
        <rect x="10" y="38" width="6" height="16" fill="var(--white)"/>
        <rect x="76" y="38" width="6" height="16" fill="var(--white)"/>
      </svg>
    </div>
    <div>
      <h2 class="capability-title">CNC LATHES</h2>
      <p class="capability-text">Tarvel Tooling is a fully equipped machine shop that has employed 4-7 people over the last three years. It is experienced in machining steel, stainless steel, aluminum, nickel and titanium. It has four CNC lathe.</p>
    </div>
  </section>

  <section class="capability capability--milling">
    <div class="capability-icon">
      <svg width="92" height="62" viewBox="0 0 92 62" fill="var(--navy)" aria-hidden="true">
        <rect x="0" y="14" width="44" height="38"/>
        <rect x="6" y="20" width="30" height="20" fill="var(--white)"/>
        <rect x="44" y="4" width="14" height="20"/>
        <rect x="49" y="24" width="4" height="10"/>
        <rect x="44" y="36" width="26" height="16"/>
        <rect x="70" y="10" width="20" height="42"/>
        <rect x="75" y="18" width="8" height="12" fill="var(--white)"/>
        <rect x="0" y="52" width="90" height="8"/>
      </svg>
    </div>
    <div>
      <h2 class="capability-title">3 &amp; 4 AXIS MILLING MACHINES</h2>
      <p class="capability-text">Tarvel Tooling is a fully equipped machine shop that has employed 4-7 people over the last three years. It is experienced in machining steel, stainless steel, aluminum, nickel and titanium. It has four CNC lathes.</p>
    </div>
  </section>

  <section class="capability capability--finishing">
    <div class="capability-icon">
      <svg width="106" height="50" viewBox="0 0 106 50" fill="var(--navy)" aria-hidden="true">
        <circle cx="40" cy="8" r="7"/>
        <circle cx="82" cy="8" r="7"/>
        <rect x="28" y="17" width="24" height="20" rx="4"/>
        <rect x="70" y="17" width="24" height="20" rx="4"/>
        <rect x="12" y="30" width="92" height="4"/>
        <rect x="14" y="40" width="8" height="8"/>
        <rect x="32" y="40" width="8" height="8"/>
        <rect x="80" y="40" width="24" height="8"/>
        <rect x="0" y="42" width="3" height="3"/>
        <rect x="5" y="42" width="3" height="3"/>
        <rect x="54" y="42" width="3" height="3"/>
        <rect x="59" y="42" width="3" height="3"/>
        <rect x="64" y="42" width="3" height="3"/>
      </svg>
    </div>
    <div>
      <h2 class="capability-title">DEBURRING, TOOLING, INSPECTION</h2>
      <p class="capability-text">Tarvel Tooling is a fully equipped machine shop that has employed 4-7 people over the last three years. It is experienced in machining steel, stainless steel, aluminum, nickel and titanium. It has four CNC lathes.</p>
    </div>
  </section>
</main>
</body>
</html>
```